Brightstep Dance Business Card

I'm looking for a two-sided business card design to promote my country dance busness. Cowboy hats, boots, and wood grain floor textures, are all appropriate to use.
On one side I want it to say:
Brightstep Dance
with
Mark
Take The Challenge - Experience The Growth
210-555-0143
On the other side I want:
A place for a Head Shot
The Quote: Experience Is The Best Teacher
A two column bullet list with the following:
First column: Two Step, Waltz, Triple Two, Polka
Second column: Cha-Cha, West Coast, East Cost, NightClub
My Name: Mark Delway
My Phone Number: 210-555-0143

```html
<!DOCTYPE html>
<html lang="en">
<head>
<meta charset="utf-8">
<title>Brightstep Dance Business Card</title>
<link rel="stylesheet" href="https://fonts.googleapis.com/css2?family=Rye&family=Alegreya+SC:wght@400;700&display=swap">
<style>
  :root {
    --page: #ececec;
    --navy: #132a4f;
    --wood-dark: #5a2a12;
    --wood-mid: #8a4422;
    --wood-light: #a35a30;
    --photo-dark: #3d2418;
    --photo-light: #8a5b40;
    --ink: #f4efe6;
  }
  * { margin: 0; padding: 0; box-sizing: border-box; }
  html, body { width: 1200px; height: 900px; overflow: hidden; background: var(--page); }
  .sheet {
    width: 1200px; height: 900px;
    display: flex; flex-direction: column; align-items: center; justify-content: center; gap: 60px;
  }
  .card { width: 630px; height: 360px; display: block; box-shadow: 0 10px 24px rgba(0,0,0,.25); }
  .display { font-family: "Rye", serif; fill: var(--ink); }
  .caps { font-family: "Alegreya SC", serif; fill: var(--ink); }
</style>
</head>
<body>
<main class="sheet">

  <!-- Front side -->
  <svg class="card card-front" viewBox="0 0 630 360" xmlns="http://www.w3.org/2000/svg">
    <defs>
      <radialGradient id="woodTone" cx="50%" cy="40%" r="75%">
        <stop offset="0" stop-color="var(--wood-light)"/>
        <stop offset=".6" stop-color="var(--wood-mid)"/>
        <stop offset="1" stop-color="var(--wood-dark)"/>
      </radialGradient>
      <path id="titleArc" d="M130 150 Q315 30 500 150"/>
    </defs>
    <rect class="wood-surface" width="630" height="360" fill="url(#woodTone)" role="img" aria-label="Wood plank floor texture background"/>
    <path class="arc-rule" d="M150 165 Q315 65 480 165" fill="none" stroke="var(--ink)" stroke-width="1.5"/>
    <text class="caps brand-line" font-size="30" font-weight="700" letter-spacing="1">
      <textPath href="#titleArc" startOffset="50%" text-anchor="middle">BRIGHTSTEP DANCE WITH</textPath>
    </text>
    <text class="display name-big" x="315" y="220" font-size="80" text-anchor="middle">MARK</text>
    <path class="ribbon" d="M60 238 H570 L555 250 L570 262 H60 L75 250 Z" fill="none" stroke="var(--ink)" stroke-width="1.5"/>
    <text class="caps tagline" x="315" y="255" font-size="14" text-anchor="middle" letter-spacing="1">Take The Challenge – Experience The Growth</text>
    <text class="display phone-big" x="315" y="315" font-size="40" text-anchor="middle">210-555-0143</text>
  </svg>

  <!-- Back side -->
  <svg class="card card-back" viewBox="0 0 630 360" xmlns="http://www.w3.org/2000/svg">
    <defs>
      <radialGradient id="photoTone" cx="45%" cy="35%" r="70%">
        <stop offset="0" stop-color="var(--photo-light)"/>
        <stop offset="1" stop-color="var(--photo-dark)"/>
      </radialGradient>
    </defs>
    <rect width="630" height="360" fill="var(--navy)"/>
    <rect class="headshot" x="20" y="20" width="280" height="320" fill="url(#photoTone)" role="img" aria-label="Head shot of Mark Delway"/>
    <text class="display headshot-name" x="40" y="320" font-size="22">MARK DELWAY</text>

    <text class="caps quote" x="330" y="72" font-size="24" font-weight="700">Experience is the</text>
    <text class="caps quote" x="330" y="102" font-size="24" font-weight="700">best teacher</text>
    <line x1="330" y1="120" x2="605" y2="120" stroke="var(--ink)" stroke-width="1"/>

    <g class="caps style-list" font-size="15">
      <text x="332" y="150">• Two Step</text>
      <text x="332" y="174">• Waltz</text>
      <text x="332" y="198">• Triple Two</text>
      <text x="332" y="222">• Polka</text>
      <text x="470" y="150">• Cha-Cha</text>
      <text x="470" y="174">• West Coast</text>
      <text x="470" y="198">• East Cost</text>
      <text x="470" y="222">• NightClub</text>
    </g>
    <line x1="330" y1="244" x2="605" y2="244" stroke="var(--ink)" stroke-width="1"/>
    <text class="display phone-big" x="468" y="300" font-size="34" text-anchor="middle">210-555-0143</text>
  </svg>

</main>
</body>
</html>
```